Menu and Logo Design for Dine in Indian restaurant

We are an Indian Restaurant(TalVir) based in Ottawa, Ontario, Canada. We would like a menu designed for our dine-in customers. The interior of the restaurant is contemporary, fine-dine, prices are slightly on the premium side. We offer quality food and generous portions. The menu design should be clear and not too busy. Some menu items shall have descriptions .

Font styles to use
Decorative
Other font styles liked:
• Devnagari font and decorative font with mandala

Colors
59FF00
82FF00
B8FF75
E3FFCB
F4FFEA
E54698
E96AAD
F1A4CE
F9D9EA
FCEFF6

```html
<!DOCTYPE html>
<html lang="en">
<head>
<meta charset="utf-8">
<title>Dine-in Menu — Cover and Speciality Dosa Page</title>
<link rel="stylesheet" href="https://fonts.googleapis.com/css2?family=Cinzel:wght@400;700&family=Cinzel+Decorative:wght@400;700&family=Lato:ital,wght@1,700&display=swap">
<style>
  :root{
    --workspace:#5c5c5c;
    --paper:#e4e1cf;
    --paper-shade:#dcd8c3;
    --gold:#a3874f;
    --gold-soft:#c9b88e;
    --gold-tint:#d3c6a0;
    --ink:#3d3a33;
    --white:#ffffff;
    --trim:#d84a4a;
  }
  *{margin:0;padding:0;box-sizing:border-box}
  html,body{width:1200px;height:865px;overflow:hidden;background:var(--workspace)}
  .canvas{position:relative;width:1200px;height:865px}
  .page{position:absolute;top:60px;width:508px;height:712px;background:var(--paper);overflow:hidden;border-top:2px solid var(--trim)}
  .page--cover{left:52px}
  .page--inside{left:650px;outline:1.5px solid #111;outline-offset:-3px}
  .frame{position:absolute;border:1.5px solid var(--gold)}
  .frame--outer{inset:19px}
  .frame--inner{inset:33px;border-width:1px;border-color:var(--gold-soft)}
  .corner{position:absolute;width:56px;height:56px;background:var(--gold-tint);border-radius:3px}
  .corner--tl{top:24px;left:24px}
  .corner--tr{top:24px;right:24px}
  .corner--bl{bottom:24px;left:24px}
  .corner--br{bottom:24px;right:24px}
  .mandala{position:absolute;left:24px;top:124px;width:460px;height:460px;border-radius:50%;background:var(--paper-shade)}
  .cartouche{position:absolute;left:112px;top:127px}
  .center{position:absolute;left:0;width:100%;text-align:center}
  .cover-col{position:absolute;left:112px;top:0;width:257px;height:712px}
  .rule{position:absolute;height:1px;background:var(--gold)}
  .rule--dashed{height:0;background:none;border-top:2px dashed var(--gold)}
  .ornament{position:absolute;left:50%;transform:translateX(-50%);background:var(--gold-tint);border-radius:40px}
  .tagline{font:700 9px/1.3 "Cinzel",serif;letter-spacing:.12em;color:var(--ink);text-transform:uppercase}
  .brand{font:700 18px/1 "Cinzel",serif;color:var(--gold);letter-spacing:.01em;text-transform:uppercase}
  .menu-title{font:400 40px/1 "Cinzel Decorative",serif;color:transparent;-webkit-text-stroke:1.3px var(--gold);letter-spacing:.04em;text-transform:uppercase}
  .subtitle{font:700 10px/1 "Cinzel",serif;letter-spacing:.14em;color:var(--ink);text-transform:uppercase}
  .web{font:700 6.5px/1 "Cinzel",serif;letter-spacing:.1em;color:var(--ink);text-transform:uppercase}
  .section-title{font:700 15px/1 "Cinzel",serif;color:var(--gold);text-transform:uppercase}
  .dish{position:absolute;width:150px}
  .dish__row{display:flex;align-items:baseline;font:700 9.5px/1 "Cinzel",serif;letter-spacing:.1em;color:var(--ink);text-transform:uppercase;white-space:nowrap}
  .dish__dots{flex:1;border-bottom:1px solid var(--ink);margin:0 4px;transform:translateY(-2px)}
  .dish__desc{margin-top:4px;font:italic 700 7px/1.3 "Lato",sans-serif;color:var(--ink)}
  .side-rule{position:absolute;top:150px;width:1px;height:420px;background:var(--gold-soft)}
</style>
</head>
<body>
<div class="canvas">

  <section class="page page--cover">
    <div class="mandala" role="img" aria-label="Faint mandala pattern behind the cover panel"></div>
    <div class="frame frame--outer"></div>
    <div class="frame frame--inner"></div>
    <div class="corner corner--tl" role="img" aria-label="Corner flourish ornament"></div>
    <div class="corner corner--tr" role="img" aria-label="Corner flourish ornament"></div>
    <div class="corner corner--bl" role="img" aria-label="Corner flourish ornament"></div>
    <div class="corner corner--br" role="img" aria-label="Corner flourish ornament"></div>

    <svg class="cartouche" width="257" height="478" viewBox="0 0 257 478">
      <path d="M70 2 Q128 -10 187 2 Q200 30 230 40 Q228 70 255 78 L255 400 Q228 408 230 438 Q200 448 187 476 Q128 488 70 476 Q57 448 27 438 Q29 408 2 400 L2 78 Q29 70 27 40 Q57 30 70 2 Z" fill="var(--white)" stroke="var(--gold)" stroke-width="2"/>
    </svg>

    <div class="cover-col">
      <div class="rule" style="left:60px;width:137px;top:189px;background:var(--gold-soft)"></div>
      <div class="rule" style="left:40px;width:177px;top:222px"></div>
      <div class="center tagline" style="top:229px">You don’t need a silver fork<br>to eat good food.</div>
      <div class="ornament" style="top:281px;width:80px;height:34px" role="img" aria-label="Floral scroll ornament above the restaurant name"></div>
      <div class="rule rule--dashed" style="left:74px;width:110px;top:321px"></div>
      <div class="center brand" style="top:331px">Restaurant Name</div>
      <div class="rule rule--dashed" style="left:74px;width:110px;top:357px"></div>
      <div class="ornament" style="top:363px;width:80px;height:32px" role="img" aria-label="Floral scroll ornament below the restaurant name"></div>
      <div class="center menu-title" style="top:424px">Menu</div>
      <div class="center subtitle" style="top:489px">Dine in Indian Restaurant</div>
      <div class="center web" style="top:504px">www.restaurantname.com</div>
      <div class="rule" style="left:60px;width:137px;top:521px;background:var(--gold-soft)"></div>
    </div>
  </section>

  <section class="page page--inside">
    <div class="frame frame--outer"></div>
    <div class="frame frame--inner"></div>
    <div class="corner corner--tl" role="img" aria-label="Corner flourish ornament"></div>
    <div class="corner corner--tr" role="img" aria-label="Corner flourish ornament"></div>
    <div class="corner corner--bl" role="img" aria-label="Corner flourish ornament"></div>
    <div class="corner corner--br" role="img" aria-label="Corner flourish ornament"></div>
    <div class="side-rule" style="left:40px"></div>
    <div class="side-rule" style="right:40px"></div>

    <div class="ornament" style="top:48px;width:80px;height:34px" role="img" aria-label="Floral scroll ornament above the restaurant name"></div>
    <div class="rule rule--dashed" style="left:199px;width:110px;top:90px"></div>
    <div class="center brand" style="top:98px">Restaurant Name</div>
    <div class="rule rule--dashed" style="left:199px;width:110px;top:124px"></div>
    <div class="ornament" style="top:130px;width:80px;height:30px" role="img" aria-label="Floral scroll ornament below the restaurant name"></div>

    <div class="rule" style="left:164px;width:180px;top:182px;background:var(--gold-soft)"></div>
    <div class="center section-title" style="top:194px">Our Speciality Dosa</div>
    <div class="rule" style="left:164px;width:180px;top:220px;background:var(--gold-soft)"></div>

    <div class="dish" style="left:97px;top:238px"><div class="dish__row">Plain Dosa<span class="dish__dots"></span>$14</div><p class="dish__desc">Lorem ipsum dolor sit amet, consectetuer adipiscing elit, sed diam nonummy</p></div>
    <div class="dish" style="left:252px;top:238px"><div class="dish__row">Plain Dosa<span class="dish__dots"></span>$14</div><p class="dish__desc">Lorem ipsum dolor sit amet, consectetuer adipiscing elit, sed diam nonummy</p></div>
    <div class="dish" style="left:97px;top:282px"><div class="dish__row">Plain Dosa<span class="dish__dots"></span>$14</div><p class="dish__desc">Lorem ipsum dolor sit amet, consectetuer adipiscing elit, sed diam nonummy</p></div>
    <div class="dish" style="left:252px;top:282px"><div class="dish__row">Plain Dosa<span class="dish__dots"></span>$14</div><p class="dish__desc">Lorem ipsum dolor sit amet, consectetuer adipiscing elit, sed diam nonummy</p></div>
    <div class="dish" style="left:97px;top:325px"><div class="dish__row">Plain Dosa<span class="dish__dots"></span>$14</div><p class="dish__desc">Lorem ipsum dolor sit amet, consectetuer adipiscing elit, sed diam nonummy</p></div>
    <div class="dish" style="left:252px;top:325px"><div class="dish__row">Plain Dosa<span class="dish__dots"></span>$14</div><p class="dish__desc">Lorem ipsum dolor sit amet, consectetuer adipiscing elit, sed diam nonummy</p></div>
    <div class="dish" style="left:97px;top:368px"><div class="dish__row">Plain Dosa<span class="dish__dots"></span>$14</div><p class="dish__desc">Lorem ipsum dolor sit amet, consectetuer adipiscing elit, sed diam nonummy</p></div>
    <div class="dish" style="left:252px;top:368px"><div class="dish__row">Plain Dosa<span class="dish__dots"></span>$14</div><p class="dish__desc">Lorem ipsum dolor sit amet, consectetuer adipiscing elit, sed diam nonummy</p></div>
  </section>

</div>
</body>
</html>
```